A website for a Maltese Law Firm

Our law firm needs a website to further its business. The site should have a simple yet effective design. We would need the following sections: About us, Practice Areas, About Malta, Contact. These should be further split as follows:

About us: Our firm, Our values, What others say, Offices

Practice Areas: Crimimal, Citizenship & Residence, Harbour Passage Scheme, Criminal Defence, Civil Litigation, Arbitration and ADR, Commercial and Corporate, Media Law.

About Malta: just one section.

Contact: Just one section

We would also need a news feed at the front of the site to include latest news regarding our cases.

At the bottom we need a section for our Terms and a Privacy Statement.

Our logo is being attached.

Target Market(s)

All clients looking for legal assistance in Malta

Industry/Entity Type

Legal

Coding

Coded - Design and coding required

Number of Pages Required

1 page

Requirements
Must have
• It must be simple yet striking.

```html
<!DOCTYPE html>
<html lang="en">
<head>
<meta charset="utf-8">
<title>Calleja &amp; Mifsud Advocates</title>
<link rel="stylesheet" href="https://fonts.googleapis.com/css2?family=Roboto:wght@400;500;700&family=Shadows+Into+Light&display=swap">
<style>
:root{
  --ink:#2b2b2b;
  --muted:#6f7378;
  --line:#d9dcdf;
  --band:#f3f4f6;
  --hero-top:#3a4466;
  --hero-bottom:#1d2236;
  --accent-line:#4f8fa6;
  --login:#3b2219;
  --button:#1f4e6e;
  --footer:#2f3438;
  --footer-text:#a9adb1;
  --white:#ffffff;
  --tile:#2a2a2a;
}
*{box-sizing:border-box;margin:0;padding:0}
html,body{width:1200px;height:2432px;overflow:hidden;background:var(--white);font-family:"Roboto",Arial,sans-serif;color:var(--ink)}
.page{position:relative;width:1200px;height:2432px}

/* header */
.site-header{position:absolute;left:0;top:0;width:1200px;height:68px;background:var(--white)}
.brand{position:absolute;left:52px;top:18px;font-size:28px;font-weight:500;letter-spacing:1px;color:var(--ink);white-space:nowrap}
.main-nav{position:absolute;top:0;height:68px;left:0;width:1200px}
.main-nav a{position:absolute;top:26px;font-size:13px;color:var(--ink);text-decoration:none;letter-spacing:.2px}
.main-nav .login{top:0;left:1103px;width:46px;height:68px;background:var(--login);color:var(--white);font-weight:700;display:flex;align-items:center;justify-content:center;font-size:12px}

/* hero */
.hero{position:absolute;left:0;top:68px;width:1200px;height:492px;background:linear-gradient(180deg,var(--hero-top),var(--hero-bottom));border-bottom:3px solid var(--accent-line);color:var(--white);text-align:center}
.hero-title{position:absolute;left:0;width:1200px;top:60px;font-family:"Shadows Into Light",cursive;font-weight:400;font-size:64px;line-height:90px;letter-spacing:2px}
.hero-lead{position:absolute;left:0;width:1200px;top:246px;font-size:20px;line-height:27px}
.hero-btn{position:absolute;top:328px;height:30px;font-size:9px;font-weight:700;display:flex;align-items:center;justify-content:center;border-radius:2px}
.hero-btn.solid{left:493px;width:71px;background:var(--white);color:var(--hero-bottom)}
.hero-btn.ghost{left:615px;width:96px;border:1px solid var(--white);color:var(--white)}
.hero-dots{position:absolute;top:458px;left:566px;display:flex;gap:10px}
.hero-dots span{width:9px;height:9px;border-radius:50%;background:var(--white)}
.hero-dots span.off{background:transparent;border:1.5px solid var(--white)}

/* intro band */
.intro{position:absolute;left:0;top:563px;width:1200px;height:366px;background:var(--band)}
.section-title{position:absolute;font-size:21px;font-weight:700;color:var(--ink)}
.rule{position:absolute;height:0;border-top:1px dashed var(--line)}
.feature{position:absolute;top:102px;width:360px;text-align:center}
.feature-icon{width:75px;height:75px;margin:0 auto;background:var(--tile);border-radius:3px;display:flex;align-items:center;justify-content:center}
.feature h3{margin-top:20px;font-size:18px;font-weight:700}
.feature p{margin:18px auto 0;width:340px;font-size:12px;line-height:19px;color:var(--muted)}

/* practice areas */
.practice-photo{position:absolute;left:50px;top:1072px;width:550px;height:379px;background:linear-gradient(135deg,#c9ccd0,#8e8f90 55%,#5a5654)}
.practice-list{position:absolute;left:616px;top:1097px;list-style:none}
.practice-list li{height:56px;display:flex;align-items:flex-start;font-size:16px;color:var(--ink)}
.chev{width:24px;height:24px;background:#eef0f2;display:flex;align-items:center;justify-content:center;margin-right:12px;margin-top:-2px}

/* news */
.news-card{position:absolute;top:1630px;width:253px;height:436px;background:var(--band)}
.news-image{height:186px}
.news-card h4{margin:16px 19px 0;font-size:17px;line-height:23px;font-weight:700}
.news-card p{margin:8px 19px 0;font-size:12px;line-height:18px;color:var(--muted);max-height:108px;overflow:hidden}
.news-date{position:absolute;left:19px;right:19px;top:393px;border-top:1px solid var(--line);padding-top:14px;font-size:11px;color:var(--muted)}
.view-more{position:absolute;left:538px;top:2077px;width:109px;height:37px;background:var(--button);color:var(--white);font-size:12px;font-weight:700;display:flex;align-items:center;justify-content:center;border-radius:3px}

/* footer */
.site-footer{position:absolute;left:0;top:2132px;width:1200px;height:300px;background:var(--footer);color:var(--footer-text)}
.footer-col{position:absolute;top:52px;width:260px}
.footer-col h5{font-size:18px;font-weight:700;color:var(--white)}
.footer-col p{margin-top:18px;font-size:13px;line-height:21px}
.footer-col b{font-weight:400;color:var(--white)}
.footer-col .second{display:block;margin-top:12px}
.social-dot{display:block;width:10px;height:10px;border-radius:50%;background:var(--footer-text);margin-top:22px}
.footer-rule{position:absolute;left:52px;right:52px;top:247px;border-top:1px solid #41474c}
.copyright{position:absolute;left:52px;top:276px;font-size:12px}
</style>
</head>
<body>
<div class="page">

  <header class="site-header">
    <div class="brand">CALLEJA &amp; MIFSUD</div>
    <nav class="main-nav">
      <a href="#" style="left:542px">ABOUT US</a>
      <a href="#" style="left:640px">OUR FIRM</a>
      <a href="#" style="left:740px">PRACTICE AREAS</a>
      <a href="#" style="left:884px">ABOUT MALTA</a>
      <a href="#" style="left:1007px">CONTACT</a>
      <a href="#" class="login">LOGIN</a>
    </nav>
  </header>

  <section class="hero" role="img" aria-label="Dark blue photograph of a statue of Justice holding a sword">
    <h1 class="hero-title">Welcome to<br>Calleja &amp; Mifsud</h1>
    <p class="hero-lead">Your trusted market research provider, dedicated to the<br>provision of meaningful and actionable insights</p>
    <a class="hero-btn solid">ABOUT US</a>
    <a class="hero-btn ghost">GO ON SURFING</a>
    <div class="hero-dots"><span></span><span class="off"></span><span></span><span></span></div>
  </section>

  <section class="intro">
    <h2 class="section-title" style="left:40px;top:26px">Calleja &amp; Mifsud Advocates</h2>
    <div class="rule" style="left:40px;width:1120px;top:60px"></div>

    <div class="feature" style="left:45px">
      <div class="feature-icon">
        <svg width="40" height="40" viewBox="0 0 40 40" fill="none" stroke="#fff" stroke-width="1.6">
          <path d="M20 5v28M12 33h16M6 10h28M20 7l-14 3M20 7l14 3"/>
          <path d="M6 10l-5 12h10zM34 10l-5 12h10z"/>
          <path d="M1 22a5 4 0 0 0 10 0M29 22a5 4 0 0 0 10 0"/>
        </svg>
      </div>
      <h3>Our firm</h3>
      <p>The quality perception of the product, what clients would like to change, what price can they afford, where is this product wanted the most, what causes dissatisfaction in a product (i.e. price, quality,design)</p>
    </div>

    <div class="feature" style="left:418px">
      <div class="feature-icon">
        <svg width="40" height="40" viewBox="0 0 40 40" fill="none" stroke="#fff" stroke-width="1.6" stroke-linejoin="round">
          <path d="M20 3l5 11 12 1-9 8 3 12-11-6-11 6 3-12-9-8 12-1z"/>
        </svg>
      </div>
      <h3>Our values</h3>
      <p>Cmadvocates is a team of law firm that work toward delivering law services while upholding the highest standards of design, analysis and reporting. Our mission is to help business in law firm</p>
    </div>

    <div class="feature" style="left:793px">
      <div class="feature-icon">
        <svg width="34" height="40" viewBox="0 0 34 40" fill="none" stroke="#fff" stroke-width="1.6" stroke-linejoin="round">
          <path d="M4 2h18l8 8v28H4z"/><path d="M22 2v8h8M10 18h14M10 24h14M10 30h14"/>
        </svg>
      </div>
      <h3>Our Offices</h3>
      <p>Our vision is to be a long-term preferred partner to our clients in the field of market law and business consulting. We are relentlessly focused on delivering exceptional value in provision of strategy, law and analysis</p>
    </div>
  </section>

  <h2 class="section-title" style="left:52px;top:998px">Practice Areas</h2>
  <div class="rule" style="left:52px;width:1096px;top:1038px"></div>
  <div class="practice-photo" role="img" aria-label="Photograph of a lawyer in a suit handing a pen to clients across a desk"></div>
  <ul class="practice-list">
    <li><span class="chev"><svg width="10" height="6" viewBox="0 0 10 6"><path d="M1 1l4 4 4-4" fill="none" stroke="#55606a" stroke-width="1.4"/></svg></span>Crimimal</li>
    <li><span class="chev"><svg width="10" height="6" viewBox="0 0 10 6"><path d="M1 1l4 4 4-4" fill="none" stroke="#55606a" stroke-width="1.4"/></svg></span>Citizenship &amp; Residence</li>
    <li><span class="chev"><svg width="10" height="6" viewBox="0 0 10 6"><path d="M1 1l4 4 4-4" fill="none" stroke="#55606a" stroke-width="1.4"/></svg></span>Harbour Passage Scheme</li>
    <li><span class="chev"><svg width="10" height="6" viewBox="0 0 10 6"><path d="M1 1l4 4 4-4" fill="none" stroke="#55606a" stroke-width="1.4"/></svg></span>Criminal Defence</li>
    <li><span class="chev"><svg width="10" height="6" viewBox="0 0 10 6"><path d="M1 1l4 4 4-4" fill="none" stroke="#55606a" stroke-width="1.4"/></svg></span>Civil Litigation</li>
    <li><span class="chev"><svg width="10" height="6" viewBox="0 0 10 6"><path d="M1 1l4 4 4-4" fill="none" stroke="#55606a" stroke-width="1.4"/></svg></span>Arbitration and ADR</li>
    <li><span class="chev"><svg width="10" height="6" viewBox="0 0 10 6"><path d="M1 1l4 4 4-4" fill="none" stroke="#55606a" stroke-width="1.4"/></svg></span>Commercial and Corporate</li>
  </ul>

  <h2 class="section-title" style="left:52px;top:1532px">Latest News</h2>
  <div class="rule" style="left:52px;width:1096px;top:1571px"></div>

  <article class="news-card" style="left:52px">
    <div class="news-image" role="img" aria-label="Red charity graphic" style="background:#e4202a"></div>
    <h4>Citizen Friendly Budgets and Budget Analysis for Children</h4>
    <p>In cooperation with Little Lanterns Trust, Northbridge Research has drafted the Citizen Friendly Budgets and Budget Analysis for Children in the Municipalities of Prishtina and Peja...</p>
    <div class="news-date">11 February, 2016</div>
  </article>

  <article class="news-card" style="left:332px">
    <div class="news-image" role="img" aria-label="Photograph of a training session with attendees at laptops" style="background:linear-gradient(160deg,#c8c9c6,#6f6c68)"></div>
    <h4>Community Needs Assessment Training</h4>
    <p>Northbridge Research is conducting a two-day training on Community Needs Assessment. This two-day training was commissioned by Civic Aid organization, and it is being delivered...</p>
    <div class="news-date">23 December, 2015</div>
  </article>

  <article class="news-card" style="left:613px">
    <div class="news-image" role="img" aria-label="Photograph of a conference room with a presentation screen" style="background:linear-gradient(160deg,#d6d8d6,#7d8583)"></div>
    <h4>Mapping of ICT Sector Labor Supply</h4>
    <p>Today during the TECHLINK Education launch event, Northbridge Research presented the findings of the study on "Mapping of ICT Sector Labor Supply and Demand"...</p>
    <div class="news-date">15 December, 2015</div>
  </article>

  <article class="news-card" style="left:895px">
    <div class="news-image" role="img" aria-label="Photograph of a speaker presenting beside a projected slide" style="background:linear-gradient(160deg,#6e5a4c,#c9c5bd 60%,#8a8581)"></div>
    <h4>Study on Impact and Sustainability of Learning Centres</h4>
    <p>Northbridge Research presented today the findings from the "Study on Impact and Sustainability of Learning Centres" to governmental representatives, international...</p>
    <div class="news-date">3 December, 2015</div>
  </article>

  <a class="view-more">VIEW MORE</a>

  <footer class="site-footer">
    <div class="footer-col" style="left:52px">
      <h5>Contact</h5>
      <p>Please feel free to contact us for any issue. Our staff is available to you from 9AM until 5PM on weekdays.</p>
      <span class="social-dot"></span>
    </div>
    <div class="footer-col" style="left:332px">
      <h5>Phone number</h5>
      <p><b>Valletta:</b> (356) 2100 0101<span class="second"><b>Birkirkara:</b> (356) 2100 0202</span></p>
    </div>
    <div class="footer-col" style="left:613px">
      <h5>Office</h5>
      <p><b>Office 1:</b> 12 Harbour Lane, Valletta<span class="second"><b>Office 2:</b> 58 Olive Street, Birkirkara</span></p>
    </div>
    <div class="footer-col" style="left:895px">
      <h5>E-Mail</h5>
      <p><b>Info:</b> info@cmadvocates.example</p>
    </div>
    <div class="footer-rule"></div>
    <div class="copyright">© 2001-2016 Cmadvocates</div>
  </footer>

</div>
</body>
</html>
```